Design a Website Mockup for Landing Page

The main goal of this website will be to collect a visitors name, email address, and phone number. It needs to appear professional and more simplistic really focusing on getting them to fill in the form and/or pressing play on the video. This needs to be where no one will have to scroll on the page before they can see this portion. Then following we will want to have testimonials and some information as the page continues. We also want to push the fact that they will be getting a free E-Book.

This is all about an Shieldpath Academy. You are welcome to visit [login to view URL] to learn more but this will be a different page that is really geared towards collecting information. We will also be adding links at the bottom such as privacy policy.

For the contest, please do not worry about the actual text on the page as it will not be the factor in winning. The one who wins will have a clean design, good choice in font style and just overall styling in convincing us to fill in the form. I will also need a simple page design to go along with it that I can place text like the privacy policy on. Thanks to everyone in advance. The FINAL version from the winner will need to be given as a PSD file.

```html
<!DOCTYPE html>
<html lang="en">
<head>
<meta charset="utf-8">
<title>Shieldpath Academy – Landing Page</title>
<link href="https://fonts.googleapis.com/css2?family=Open+Sans:wght@400;600;700&display=swap" rel="stylesheet">
<style>
  :root{
    --brand-red:#c8161d;
    --hero-red:#b3161c;
    --hero-glow:#e23a3a;
    --ink:#222;
    --body-text:#666;
    --muted:#999;
    --rule:#e6e6e6;
    --panel-dark:#1e1e1e;
    --footer-bg:#2b2b2b;
    --footer-bar:#353535;
    --footer-text:#cfcfcf;
    --white:#fff;
  }
  *{box-sizing:border-box;margin:0;padding:0}
  html,body{width:981px;height:1200px;overflow:hidden}
  body{position:relative;background:var(--white);font-family:'Open Sans',Arial,sans-serif;color:var(--ink)}
  .abs{position:absolute}

  /* Header */
  .site-header{left:0;top:0;width:981px;height:48px;background:var(--white)}
  .brand{left:228px;top:10px;width:110px;font-weight:700;font-size:13px;letter-spacing:.5px;color:var(--brand-red);text-transform:uppercase;line-height:14px}
  .main-nav{left:414px;top:0;width:339px;height:48px;display:flex;justify-content:space-between;align-items:center}
  .main-nav a{font-size:7px;color:#333;text-decoration:none;position:relative;line-height:48px;white-space:nowrap}
  .main-nav a.is-active{color:var(--brand-red)}
  .main-nav a.is-active::after{content:"";position:absolute;left:0;right:0;bottom:12px;height:1px;background:var(--brand-red)}

  /* Hero */
  .hero{left:0;top:48px;width:981px;height:241px;background:radial-gradient(ellipse 260px 200px at 400px 0,var(--hero-glow),var(--hero-red) 70%)}
  .video{left:228px;top:76px;width:337px;height:213px;background:#0e1115;border:2px solid #111}
  .video-still{position:absolute;left:0;top:0;width:333px;height:190px;background:linear-gradient(180deg,#3d4b57,#20272e 70%,#15191d)}
  .play-btn{position:absolute;left:147px;top:77px}
  .video-bar{position:absolute;left:0;bottom:0;width:333px;height:19px;background:#111;display:flex;align-items:center;gap:8px;padding:0 6px;color:#bbb;font-size:5.5px}
  .video-bar .track{position:absolute;left:0;top:-3px;width:333px;height:2px;background:#444}
  .video-bar .spacer{flex:1}

  .lead-form{left:601px;top:76px;width:151px;height:213px;background:var(--panel-dark);padding:10px 5px 0}
  .field-label{display:block;color:var(--white);font-size:6px;margin-bottom:4px}
  .field{position:relative;height:21px;background:var(--white);border:1px solid var(--brand-red);margin-bottom:18px;font-size:5.5px;color:#888;padding:0 10px;line-height:19px}
  .field svg{position:absolute;right:6px;top:5px}
  .submit-btn{height:23px;background:var(--brand-red);border:1px solid #e44;color:var(--white);font-size:6px;font-weight:700;text-align:center;line-height:21px;margin-top:6px}

  /* Features */
  .features{left:228px;top:313px;width:530px;display:flex}
  .feature{width:185px}
  .feature h3{font-size:8.5px;font-weight:700;display:flex;align-items:center;gap:5px;margin-bottom:10px}
  .feature p{font-size:6.5px;line-height:11px;color:var(--body-text);width:145px}
  .section-rule{left:0;width:981px;height:1px;background:var(--rule)}

  /* About */
  .about-art{left:240px;top:441px;width:212px;height:153px;background:linear-gradient(135deg,#f4f4f4,#d8d8d8 60%,#3a3a3a);border-radius:4px}
  .about-title{left:471px;top:427px;font-size:14px;font-weight:600;letter-spacing:1px}
  .mini-rule{left:471px;width:84px;height:6px;border:1px solid #eee;background:#fafafa}
  .about-text{left:471px;top:484px;width:250px;font-size:6.5px;line-height:11px;color:var(--body-text)}
  .about-text p+p{margin-top:5px}
  .btn-outline{left:471px;top:598px;width:71px;height:23px;border:1px solid #bbb;font-size:6.5px;color:#444;text-align:center;line-height:21px}

  /* Testimonials */
  .testi-title{left:0;width:981px;top:686px;text-align:center;font-size:14px;font-weight:600;letter-spacing:1px}
  .testi-rule{left:405px;top:722px;width:171px;height:1px;background:var(--rule)}
  .testi-grid{left:228px;top:747px;width:530px;height:169px}
  .testi-grid .vline{position:absolute;left:261px;top:0;width:1px;height:169px;background:#eee}
  .testi-grid .hline{position:absolute;left:0;top:89px;width:530px;height:1px;background:#eee}
  .testimonial{position:absolute;display:flex;gap:11px}
  .avatar{width:41px;height:41px;border-radius:50%;background:linear-gradient(160deg,#d9d3cc,#7d7570);flex:none;margin-top:7px}
  .testimonial blockquote{font-size:6.3px;line-height:11px;color:var(--body-text)}
  .testimonial .who{font-size:6.3px;margin-top:6px;color:#333;line-height:11px}
  .testimonial .who strong{font-weight:600;display:block}
  .testimonial .who span{color:var(--brand-red)}

  /* Footer */
  .site-footer{left:0;top:994px;width:981px;height:179px;background:var(--footer-bg);color:var(--footer-text)}
  .footer-col{position:absolute;top:28px;font-size:6.5px;line-height:11px}
  .footer-col h4{font-size:7px;font-weight:400;letter-spacing:1px;color:#999;margin-bottom:11px}
  .footer-brand{font-weight:700;font-size:13px;color:var(--white);text-transform:uppercase;line-height:14px;margin-bottom:8px}
  .news-item{display:flex;gap:7px;margin-bottom:8px}
  .news-thumb{width:17px;height:17px;background:linear-gradient(135deg,#8b6b4a,#3c4a5a);border:1px solid #555;flex:none}
  .news-item small{display:block;font-size:4.5px;color:#888;line-height:8px}
  .news-item div{font-size:5.5px;line-height:8px;color:#ddd}
  .sitemap a{display:block;color:var(--white);text-decoration:none;font-weight:600;font-size:6.5px;line-height:18px}
  .hours strong{color:var(--white);font-weight:600}
  .to-top{left:784px;top:1148px;width:25px;height:25px;background:#3a3a3a}
  .footer-bar{left:0;top:1173px;width:981px;height:27px;background:var(--footer-bar);color:#ccc;font-size:5.5px}
  .footer-bar .copy{position:absolute;left:228px;top:9px}
  .socials{position:absolute;right:228px;top:5px;display:flex;gap:7px}
  .socials span{width:17px;height:17px;background:var(--brand-red)}
</style>
</head>
<body>

<header class="site-header abs">
  <div class="brand abs">Shieldpath<br>Academy</div>
  <nav class="main-nav abs">
    <a class="is-active" href="#">Introduction</a>
    <a href="#">All Insurances</a>
    <a href="#">Curriculum</a>
    <a href="#">Connecting the Dots</a>
    <a href="#">Show Me the Money</a>
    <a href="#">Contact</a>
  </nav>
</header>

<section class="hero abs"></section>

<div class="video abs">
  <div class="video-still" role="img" aria-label="Video still: business people holding black umbrellas in the rain"></div>
  <svg class="play-btn" width="40" height="40" viewBox="0 0 40 40" aria-hidden="true">
    <circle cx="20" cy="20" r="19" fill="#c8161d" stroke="#fff" stroke-width="2"/>
    <path d="M15 11 L29 20 L15 29 Z" fill="#fff"/>
  </svg>
  <div class="video-bar">
    <div class="track"></div>
    <svg width="6" height="7" aria-hidden="true"><rect x="0" y="0" width="2" height="7" fill="#ccc"/><rect x="4" y="0" width="2" height="7" fill="#ccc"/></svg>
    <svg width="9" height="7" aria-hidden="true"><path d="M0 2h2l3-2v7L2 5H0z" fill="#ccc"/><path d="M6.5 1.5q2 2 0 4" stroke="#ccc" fill="none"/></svg>
    <span>00:00 / 11:58</span>
    <span class="spacer"></span>
    <span>360p</span>
    <svg width="7" height="7" aria-hidden="true"><path d="M0 2V0h2M5 0h2v2M7 5v2H5M2 7H0V5" stroke="#ccc" fill="none"/></svg>
  </div>
</div>

<form class="lead-form abs">
  <label class="field-label">Full Name</label>
  <div class="field">type your full name
    <svg width="9" height="9" viewBox="0 0 9 9" aria-hidden="true"><circle cx="4.5" cy="2.5" r="2.2" fill="#333"/><path d="M0.5 9q0-4 4-4t4 4z" fill="#333"/></svg>
  </div>
  <label class="field-label">Email Address</label>
  <div class="field">type your email address
    <svg width="10" height="8" viewBox="0 0 10 8" aria-hidden="true"><rect x="0.5" y="0.5" width="9" height="7" fill="none" stroke="#333"/><path d="M0.5 0.5l4.5 4 4.5-4" fill="none" stroke="#333"/></svg>
  </div>
  <label class="field-label">Phone Number</label>
  <div class="field">type your phone no
    <svg width="9" height="9" viewBox="0 0 9 9" aria-hidden="true"><path d="M1 1.5l2-1 1.2 2.2-1 .8q.8 1.7 2.3 2.3l.8-1 2.2 1.2-1 2Q3 8 1 1.5z" fill="#333"/></svg>
  </div>
  <div class="submit-btn">SUBMIT!</div>
</form>

<section class="features abs">
  <div class="feature">
    <h3><svg width="10" height="10" aria-hidden="true"><circle cx="5" cy="5" r="4.3" fill="none" stroke="#222"/><text x="5" y="7.5" font-size="7" text-anchor="middle" font-family="Open Sans, sans-serif">?</text></svg>LORME IPSUM 1</h3>
    <p>Lorem Ipsum passage, and going through the cites of the word in classical literature, discovered the undoubtable source.</p>
  </div>
  <div class="feature">
    <h3><svg width="10" height="10" aria-hidden="true"><circle cx="5" cy="5" r="4.3" fill="none" stroke="#222" stroke-dasharray="3 1.5"/><circle cx="5" cy="5" r="1.6" fill="#222"/></svg>LORME IPSUM 2</h3>
    <p>Lorem Ipsum passage, and going through the cites of the word in classical literature, discovered the undoubtable source.</p>
  </div>
  <div class="feature">
    <h3><svg width="10" height="10" aria-hidden="true"><rect x="1" y="1" width="8" height="8" fill="none" stroke="#222"/><path d="M3 4h4M3 6h4" stroke="#222"/></svg>LORME IPSUM 3</h3>
    <p>Lorem Ipsum passage, and going through the cites of the word in classical literature, discovered the undoubtable source.</p>
  </div>
</section>

<div class="section-rule abs" style="top:390px"></div>

<div class="about-art abs" role="img" aria-label="Illustration: businessman leaning on a large umbrella sheltering a small house"></div>
<h2 class="about-title abs">ABOUT US</h2>
<div class="mini-rule abs" style="top:459px"></div>
<div class="about-text abs">
  <p>Lorem ipsum dolor sit amet, consectetuer adipiscing elit. Aenena commodo ligula eget dolor. Aenean massa.</p>
  <p>Many desktop publishing packages and web page editors now use Lorem Ipsum as their default model text, and a search for 'lorem ipsum' will uncover many web sites still in their infancy. Various versions have evolved over the years, sometimes by accident.</p>
</div>
<div class="mini-rule abs" style="top:572px"></div>
<div class="btn-outline abs">Read More</div>

<div class="section-rule abs" style="top:652px"></div>

<h2 class="testi-title abs">TESTIMONIALS</h2>
<div class="testi-rule abs"></div>

<section class="testi-grid abs">
  <div class="vline"></div>
  <div class="hline"></div>
  <div class="testimonial" style="left:10px;top:0;width:240px">
    <div class="avatar" role="img" aria-label="Portrait photo of the client"></div>
    <div>
      <blockquote>Nulla consequat massa quis enim. Donec pede justo, fringilla vel, aliquet nec, vulputate eget, arcu. In enim justo, rhoncus ut, imperdiet a, venenatis vitae, justo. Nullam dictum felis eu pede mollis pretium. Integer tincidunt. Cras dapibus.</blockquote>
      <div class="who"><strong>Helen R. Carver</strong>Marketing – <span>Roamly</span></div>
    </div>
  </div>
  <div class="testimonial" style="left:272px;top:0;width:250px">
    <div class="avatar" role="img" aria-label="Portrait photo of the client"></div>
    <div>
      <blockquote>In enim justo, rhoncus ut, imperdiet a, venenatis vitae, justo. Nullam dictum felis eu pede mollis pretium. Integer tincidunt. Cras dapibus.</blockquote>
      <div class="who"><strong>Nora Velasquez</strong>CEO – <span>Pressfield</span></div>
    </div>
  </div>
  <div class="testimonial" style="left:10px;top:90px;width:240px">
    <div class="avatar" role="img" aria-label="Portrait photo of the client"></div>
    <div>
      <blockquote>Nulla consequat massa quis enim. Donec pede justo, fringilla vel, aliquet nec, vulputate eget, arcu.</blockquote>
      <div class="who"><strong>Tomas Reyes</strong>Public Relations – <span>Linkwave</span></div>
    </div>
  </div>
  <div class="testimonial" style="left:272px;top:90px;width:250px">
    <div class="avatar" role="img" aria-label="Portrait photo of the client"></div>
    <div>
      <blockquote>In enim justo, rhoncus ut, imperdiet a, venenatis vitae, justo. Nullam dictum felis eu pede mollis pretium. Integer tincidunt. Cras dapibus.</blockquote>
      <div class="who"><strong>Dr. Adeyemi</strong>Dean of Medicine – <span>Northgate Clinic</span></div>
    </div>
  </div>
</section>

<footer class="site-footer abs">
  <div class="footer-col" style="left:228px;width:115px">
    <h4>ABOUT US</h4>
    <div class="footer-brand">Shieldpath<br>Academy</div>
    <p>Lorem Ipsum as their default model text, and a search for 'lorem ipsum' will uncover many web sites still in their infancy.</p>
  </div>
  <div class="footer-col" style="left:377px;width:115px">
    <h4>LATEST NEWS</h4>
    <div class="news-item"><span class="news-thumb" role="img" aria-label="Post thumbnail"></span><div>Postformat Gallery: Multiple images<small>October 21, 2013 - 3:31 pm</small></div></div>
    <div class="news-item"><span class="news-thumb" role="img" aria-label="Post thumbnail"></span><div>Snowboarding is fun!<small>December 12, 2012 - 9:11 pm</small></div></div>
    <div class="news-item"><span class="news-thumb" role="img" aria-label="Post thumbnail"></span><div>This is a standard post format with preview Picture<small>January 14, 2012 - 1:13 pm</small></div></div>
  </div>
  <div class="footer-col sitemap" style="left:527px;width:100px">
    <h4 style="margin-bottom:4px">SITEMAP</h4>
    <a href="#">Introduction</a>
    <a href="#">All Insurances</a>
    <a href="#">Curriculum</a>
    <a href="#">Connecting the Dots</a>
    <a href="#">Connecting the Dots</a>
    <a href="#">Contact</a>
  </div>
  <div class="footer-col hours" style="left:646px;width:115px">
    <h4>BUSINESS HOURS</h4>
    <p style="color:#fff">Our support Hotline is available 24 Hours a day: (555) 210 884 3150</p>
    <p style="margin-top:11px"><strong>Monday-Friday:</strong> 9am to 5pm<br><strong>Saturday:</strong> 10am to 2pm<br><strong>Sunday:</strong> Closed</p>
  </div>
</footer>

<div class="to-top abs"><svg width="25" height="25" aria-hidden="true"><path d="M10.5 14l2-2 2 2" stroke="#aaa" fill="none"/></svg></div>

<div class="footer-bar abs">
  <span class="copy">© Copyright - 2015 - Shieldpath Academy</span>
  <div class="socials" role="img" aria-label="Social network links">
    <span></span><span></span><span></span><span></span><span></span>
  </div>
</div>

</body>
</html>
```